Business Card Re-design

We are looking for a fresh bold look for general office business cards. We are a staffing agency that staffs industrial, coal mining, and clerical jobs.
Tag Line: We connect the RIGHT people with the RIGHT jobs.
Evansville Office: 2473 W. Tallow Creek Rd, Evansville, IN - 47308
p. 555.203.6180 f. 555.203.6195
Princeton Office: 264 S. Birch Ln, Princeton, IN - 47152
p. 555.319.2047 f. 555.203.6195
Absentee/Emergency 24hr Hotline 555.203.6172 opt.1
www.bluelanternworkforce.example

```html
<!DOCTYPE html>
<html lang="en">
<head>
<meta charset="utf-8">
<title>Blue Lantern Workforce – Business Card</title>
<link href="https://fonts.googleapis.com/css2?family=Chewy&family=Open+Sans:wght@400;600;700&display=swap" rel="stylesheet">
<style>
  :root {
    --backdrop: #e9e6e1;
    --navy: #0b2148;
    --navy-deep: #06183a;
    --blue: #3f6aa6;
    --sky: #8cc9ea;
    --green: #5cb947;
    --green-light: #8fd16a;
    --ink: #2b2f36;
    --paper: #ffffff;
  }
  * { box-sizing: border-box; margin: 0; padding: 0; }
  html, body { width: 1200px; height: 1200px; overflow: hidden; }
  body {
    background: var(--backdrop);
    display: flex;
    flex-direction: column;
    align-items: center;
    justify-content: center;
    gap: 56px;
    font-family: "Open Sans", sans-serif;
  }
  .card {
    position: relative;
    width: 900px;
    height: 514px;
    border-radius: 36px;
    overflow: hidden;
    box-shadow: 0 10px 24px rgba(0,0,0,0.18);
  }
  .card-stripes { position: absolute; inset: 0; width: 100%; height: 100%; }

  /* Front */
  .card--front { background: linear-gradient(120deg, #0d3260 0%, var(--navy) 45%, var(--navy-deep) 100%); }
  .tagline {
    position: absolute;
    left: 90px;
    top: 200px;
    font-family: "Chewy", sans-serif;
    font-size: 44px;
    line-height: 1.2;
    color: var(--paper);
    letter-spacing: 1px;
  }
  .tagline-line--second { padding-left: 28px; }
  .tagline-accent { color: var(--green-light); }

  /* Back */
  .card--back { background: var(--paper); }
  .offices {
    position: absolute;
    right: 56px;
    top: 36px;
    text-align: right;
    font-size: 17px;
    line-height: 1.45;
    color: var(--ink);
  }
  .office + .office { margin-top: 16px; }
  .label { color: var(--blue); font-weight: 600; }
  .brand {
    position: absolute;
    right: 56px;
    top: 268px;
    display: flex;
    align-items: center;
    gap: 16px;
  }
  .brand-mark { width: 30px; height: 30px; background: var(--green); }
  .brand-name {
    font-weight: 700;
    font-size: 40px;
    line-height: 1.05;
    color: var(--navy);
    text-align: right;
  }
  .hotline {
    position: absolute;
    left: 290px;
    bottom: 36px;
    width: 400px;
    color: var(--ink);
  }
  .hotline-number, .hotline-web {
    text-align: right;
    font-size: 18px;
    line-height: 1.4;
  }
  .hotline-rule { height: 2px; background: var(--sky); margin: 8px 0; }
  .hotline-title {
    font-weight: 700;
    font-size: 20px;
    letter-spacing: 0.3px;
    white-space: nowrap;
  }
  .hotline-accent { color: var(--green); }
</style>
</head>
<body>

  <section class="card card--front" aria-label="Card front">
    <svg class="card-stripes" viewBox="0 0 900 514" aria-hidden="true">
      <defs>
        <linearGradient id="front-blue" x1="0" y1="0" x2="0" y2="1">
          <stop offset="0" stop-color="#3a5f9c"/>
          <stop offset="1" stop-color="#8cc9ea"/>
        </linearGradient>
        <linearGradient id="front-green" x1="0" y1="0" x2="0" y2="1">
          <stop offset="0" stop-color="#4aa93c"/>
          <stop offset="1" stop-color="#8fd16a"/>
        </linearGradient>
      </defs>
      <polygon points="700,0 810,0 650,514 540,514" fill="url(#front-blue)"/>
      <polygon points="850,0 930,0 770,514 690,514" fill="url(#front-green)"/>
    </svg>
    <p class="tagline">
      <span class="tagline-line">We connect the <span class="tagline-accent">RIGHT</span> people</span><br>
      <span class="tagline-line tagline-line--second">with the RIGHT jobs.</span>
    </p>
  </section>

  <section class="card card--back" aria-label="Card back">
    <svg class="card-stripes" viewBox="0 0 900 514" aria-hidden="true">
      <defs>
        <linearGradient id="back-blue" x1="0" y1="0" x2="0" y2="1">
          <stop offset="0" stop-color="#8cc9ea"/>
          <stop offset="1" stop-color="#2e4f8f"/>
        </linearGradient>
        <linearGradient id="back-green" x1="0" y1="0" x2="0" y2="1">
          <stop offset="0" stop-color="#8fd16a"/>
          <stop offset="1" stop-color="#4aa93c"/>
        </linearGradient>
      </defs>
      <polygon points="70,150 150,150 0,634 0,376" fill="url(#back-green)"/>
      <polygon points="235,150 350,150 190,664 75,664" fill="url(#back-blue)"/>
    </svg>

    <div class="offices">
      <div class="office">
        <p>Evansville Office</p>
        <p>2473 W. Tallow Creek Rd</p>
        <p>Evansville, IN - 47308</p>
        <p><span class="label">T.</span> 555.203.6180 | <span class="label">F.</span> 555.203.6195</p>
      </div>
      <div class="office">
        <p>Princeton Office</p>
        <p>264 S. Birch Ln, Princeton, IN - 47152</p>
        <p><span class="label">T.</span> 555.319.2047 | <span class="label">F.</span> 555.203.6195</p>
      </div>
    </div>

    <div class="brand">
      <span class="brand-mark" aria-hidden="true"></span>
      <p class="brand-name">Blue Lantern<br>Workforce</p>
    </div>

    <div class="hotline">
      <p class="hotline-number">555.203.6172 opt.1</p>
      <p class="hotline-web">www.bluelanternworkforce.example</p>
      <div class="hotline-rule"></div>
      <p class="hotline-title">ABSENTEE/EMERGENCY <span class="hotline-accent">24HR</span> HOTLINE</p>
    </div>
  </section>

</body>
</html>
```